Stationery Design Project

Require letterhead/stationery design based on new logo (see attached).

Would prefer it kept simple but strong and effective.

Target Market(s)

Clients and building developers. Residential/consumer and corporate clientele.

```html
<!DOCTYPE html>
<html lang="en">
<head>
<meta charset="utf-8">
<title>Strataform Builders — Letterhead</title>
<link href="https://fonts.googleapis.com/css2?family=Questrial&display=swap" rel="stylesheet">
<style>
  :root {
    --backdrop: #ececec;
    --paper: #fafafa;
    --mark-bg: #2b2b2b;
    --mark-text: #c9c9c9;
    --ink: #3a3a3a;
    --rule: #6a6a6a;
  }
  * { margin: 0; padding: 0; box-sizing: border-box; }
  html, body {
    width: 1200px;
    height: 936px;
    overflow: hidden;
    background: var(--backdrop);
    font-family: "Questrial", sans-serif;
  }
  .letterhead {
    position: absolute;
    left: 300px;
    top: 44px;
    width: 600px;
    height: 848px;
    background: var(--paper);
    box-shadow: 0 2px 10px rgba(0,0,0,0.08);
  }
  .brand-block {
    position: absolute;
    left: 236px;
    top: 34px;
    width: 128px;
    height: 128px;
    background: var(--mark-bg);
    display: flex;
    flex-direction: column;
    align-items: center;
    justify-content: center;
    gap: 4px;
  }
  .brand-name {
    color: var(--mark-text);
    font-size: 13px;
    letter-spacing: 0.12em;
    text-transform: uppercase;
    text-align: center;
    line-height: 1.3;
  }
  .footer {
    position: absolute;
    left: 64px;
    right: 48px;
    bottom: 46px;
  }
  .footer-rule {
    border-top: 1px solid var(--rule);
    margin-bottom: 6px;
  }
  .contact {
    display: flex;
    justify-content: space-between;
    align-items: center;
    font-size: 8.5px;
    color: var(--ink);
    letter-spacing: 0.02em;
  }
  .contact-phone {
    display: flex;
    align-items: center;
    gap: 4px;
  }
  .phone-icon { width: 9px; height: 9px; }
</style>
</head>
<body>
  <main class="letterhead">
    <div class="brand-block">
      <span class="brand-name">Strataform<br>Builders</span>
    </div>

    <footer class="footer">
      <div class="footer-rule"></div>
      <div class="contact">
        <span class="contact-address">18/4, Near Harbour Road, Kalvi Nagar, Westbay, U.T. OF CORALIA - 482517</span>
        <span class="contact-phone">
          <svg class="phone-icon" viewBox="0 0 10 10" aria-hidden="true">
            <circle cx="5" cy="5" r="4.5" fill="none" stroke="#3a3a3a" stroke-width="1"/>
            <path d="M3.3 2.8 L4.2 2.6 L4.6 3.8 L4 4.2 Q4.5 5.5 5.8 6 L6.2 5.4 L7.4 5.8 L7.2 6.7 Q5.8 7.4 4.2 5.8 Q2.6 4.2 3.3 2.8 Z" fill="#3a3a3a"/>
          </svg>
          +91 274 3186520
        </span>
      </div>
    </footer>
  </main>
</body>
</html>
```